Static landing page for our consulting business

Hi

I require a website for a company called "Koblane (Pty) Ltd"
It is a management consulting company with three core consulting services.
1. IT
2. Finance
3. Engineering

Our webpage basically needs a landing page with an overview and history of the company.

Then a sub section for each of the three disciplines with a description of what services are rendered. Each of these sections needs to have a link to the consultant that heads up that discipline.

Each consultant of which there are 3 potentially four shortly then needs a page that could introduce themselves, their qualifications etc.

There would also be a 'contact us & information page'
I have attached company logo for your reference.

Target Market(s)

Finance and management consulting

Industry/Entity Type

Business

Coding

Coded - Design and coding required

Number of Pages Required

1 page

Font styles to use
Sans Serif

Colors
33a6d7
85cae6
f68d4d
0492cd
f37122

Requirements
Must have
• basic html page with CSS, no back end or .net. Would run on a php server, and we would add the dynamic content ourselves if required later.
Nice to have
• Social media links, we would code them later.

```html
<!DOCTYPE html>
<html lang="en">
<head>
<meta charset="utf-8">
<title>Koblane (Pty) Ltd — Management Consulting</title>
<link href="https://fonts.googleapis.com/css2?family=Open+Sans:wght@400;600;700;800&display=swap" rel="stylesheet">
<style>
:root{
  --blue:#0492cd;
  --blue-mid:#33a6d7;
  --blue-light:#85cae6;
  --blue-deep:#0a7fb4;
  --orange:#f37122;
  --orange-soft:#f68d4d;
  --ink:#2f3338;
  --text:#777c82;
  --line:#e3e6e9;
  --pale:#eef2f5;
  --footer:#2a2d30;
  --footer-deep:#1f2124;
  --white:#ffffff;
}
*{box-sizing:border-box;margin:0;padding:0}
html,body{width:1200px;height:2292px;overflow:hidden}
body{font-family:"Open Sans",Arial,sans-serif;color:var(--text);background:var(--white);font-size:12px;line-height:1.7}
a{color:inherit;text-decoration:none}
.container{width:1000px;margin:0 auto;position:relative}

/* header */
.site-header{height:68px;background:var(--white);border-bottom:1px solid var(--line)}
.site-header .container{display:flex;align-items:center;justify-content:space-between;height:68px}
.brand{display:flex;align-items:center;gap:8px;font-weight:800;font-size:26px;color:var(--ink);letter-spacing:-.5px}
.brand-dot{width:12px;height:12px;border-radius:50%;background:var(--blue)}
.main-nav{display:flex;align-items:center;gap:26px;font-size:11px;font-weight:700;color:var(--ink);text-transform:uppercase}
.main-nav .active{color:var(--blue)}

/* hero */
.hero{height:672px;position:relative;background:linear-gradient(90deg,#f4f6f8 0%,#eef1f4 35%,#dfe5ea 100%);overflow:hidden}
.hero-photo{position:absolute;left:380px;top:0;width:820px;height:672px;background:radial-gradient(ellipse at 60% 45%,#5d6670 0%,#a7b0b8 45%,#dfe4e8 80%)}
.hero-copy{position:absolute;left:100px;top:210px;width:340px}
.hero-copy h1{font-size:32px;font-weight:800;color:var(--ink);letter-spacing:.5px;line-height:1.2}
.hero-copy h2{font-size:17px;font-weight:700;color:var(--blue);margin:4px 0 12px;line-height:1.3}
.hero-copy p{font-size:11px;line-height:1.7}
.hero-actions{display:flex;gap:10px;margin-top:34px}
.btn{display:inline-block;font-size:10px;font-weight:700;text-transform:uppercase;padding:9px 20px;border-radius:2px}
.btn-outline{border:1px solid var(--blue);color:var(--blue);background:var(--white)}
.btn-solid{background:var(--blue);color:var(--white)}
.hero-arrow{position:absolute;top:418px;width:24px;height:24px}
.hero-arrow.prev{left:28px}.hero-arrow.next{right:28px}

/* services */
.services{display:flex;height:260px}
.service{flex:1;color:var(--white);text-align:center;padding:34px 60px 0}
.service.it{background:var(--blue-mid)}
.service.finance{background:#4fb6e0}
.service.engineering{background:var(--blue)}
.service svg{width:56px;height:56px;display:block;margin:0 auto 14px}
.service h3{font-size:11px;font-weight:700;text-transform:uppercase;margin-bottom:8px}
.service p{font-size:10px;line-height:1.7;opacity:.92}
.service .more{display:inline-block;margin-top:8px;font-size:10px;font-weight:700}

/* about */
.about{height:400px;padding-top:60px}
.about .container{display:flex;gap:60px}
.about-visual{width:240px;height:330px;flex:none}
.about-screen{width:230px;height:160px;border:8px solid #1e2226;border-radius:6px;background:linear-gradient(135deg,#6b7580,#c4cbd1)}
.about-stand{width:50px;height:40px;margin:0 auto;background:linear-gradient(#cfd4d8,#aeb5bb)}
.about-base{width:110px;height:6px;margin:0 auto;background:#aeb5bb;border-radius:3px}
.about-copy h2{font-size:18px;font-weight:700;color:var(--ink);margin-top:8px}
.about-copy h4{font-size:10px;font-weight:700;color:var(--blue);text-transform:uppercase;margin:2px 0 12px}
.about-copy p{font-size:10.5px;margin-bottom:10px;line-height:1.75}
.about-copy .btn{margin-top:8px}

/* testimonials */
.testimonials{height:300px;background:var(--pale);text-align:center;padding-top:52px}
.section-title{font-size:18px;font-weight:700;color:var(--ink);text-transform:uppercase}
.rule{width:60px;height:2px;background:var(--blue);margin:10px auto 26px}
.testimonials blockquote{width:860px;margin:0 auto;font-size:11px;line-height:1.8;position:relative}
.quote-mark{display:inline-block;vertical-align:top;margin-right:6px}
.testimonials cite{display:block;font-style:normal;font-weight:700;color:var(--ink);font-size:11px;margin-top:16px}
.testimonials .role{font-size:10px}
.dots{display:flex;gap:6px;justify-content:center;margin-top:12px}
.dots span{width:8px;height:8px;border-radius:50%;background:var(--blue-light)}
.dots span.on{background:var(--blue)}

/* news */
.news{height:300px;padding-top:64px}
.news .section-title{text-align:left}
.news .rule{margin:10px 0 40px}
.news-list{display:flex;gap:60px}
.news-item{display:flex;gap:14px;width:293px}
.news-date{width:74px;flex:none;text-align:center;color:var(--white);font-weight:700}
.news-date .day{display:block;background:var(--blue-mid);font-size:14px;padding:8px 0}
.news-date .year{display:block;background:var(--blue);font-size:11px;padding:4px 0}
.news-item h5{font-size:10px;font-weight:700;color:var(--blue);text-transform:uppercase;margin-bottom:4px;line-height:1.4}
.news-item p{font-size:10px;line-height:1.6}

/* footer */
.site-footer{height:240px;background:var(--footer);color:#b4b8bc;padding-top:32px}
.site-footer .container{display:flex}
.foot-col{font-size:10.5px}
.foot-col h6{font-size:13px;font-weight:600;color:var(--white);margin-bottom:14px}
.foot-col ul{list-style:none;line-height:1.9}
.col-links{width:160px}
.col-news{width:280px}
.col-follow{width:240px}
.col-contact{width:320px}
.news-input{width:150px;height:24px;border:1px solid #4a4e52;background:#363a3e;color:#8d9297;font-size:10px;padding:4px 8px;margin:10px 0 8px}
.foot-col .btn{padding:6px 12px;font-size:9px}
.social li,.contact li{display:flex;align-items:center;gap:10px;margin-bottom:4px}
.icon-dot{width:14px;height:14px;border-radius:50%;background:var(--blue-mid);flex:none}
.contact svg{width:14px;height:14px;flex:none}
.copyright{height:52px;background:var(--footer-deep);color:#8d9297;font-size:10px;text-align:center;line-height:52px}
</style>
</head>
<body>

<header class="site-header">
  <div class="container">
    <a class="brand" href="#"><span class="brand-dot"></span>Koblane</a>
    <nav class="main-nav">
      <a class="active" href="#">Home</a>
      <a href="#">About Us</a>
      <a href="#">Services</a>
      <a href="#">Testimonials</a>
      <a href="#">News</a>
      <a href="#">Contact Us</a>
      <svg width="13" height="13" viewBox="0 0 13 13" fill="none" stroke="#0492cd" stroke-width="2"><circle cx="5.5" cy="5.5" r="4"/><path d="M8.5 8.5L12 12"/></svg>
    </nav>
  </div>
</header>

<section class="hero">
  <div class="hero-photo" role="img" aria-label="Photo of two business consultants reviewing a tablet in a bright office"></div>
  <svg class="hero-arrow prev" viewBox="0 0 24 24" fill="none" stroke="#ffffff" stroke-width="3"><path d="M16 3L7 12l9 9"/></svg>
  <svg class="hero-arrow next" viewBox="0 0 24 24" fill="none" stroke="#ffffff" stroke-width="3"><path d="M8 3l9 9-9 9"/></svg>
  <div class="hero-copy">
    <h1>KOBLANE</h1>
    <h2>SED UT PERSPICIATIS UNDE OMNIS ISTE</h2>
    <p>We partner with growing businesses to sharpen strategy, strengthen finance and modernise systems, delivering measurable results through hands-on consulting.</p>
    <div class="hero-actions">
      <a class="btn btn-outline" href="#">Read More</a>
      <a class="btn btn-solid" href="#">Free Consultation</a>
    </div>
  </div>
</section>

<section class="services">
  <div class="service it">
    <svg viewBox="0 0 56 56" fill="none" stroke="#fff" stroke-width="3"><rect x="8" y="10" width="40" height="28" rx="2"/><path d="M22 46h12M28 38v8"/></svg>
    <h3>Information Technology</h3>
    <p>Practical technology advice covering systems audits, infrastructure planning, software selection and digital projects that keep your operations running smoothly.</p>
    <a class="more" href="#">Read more »</a>
  </div>
  <div class="service finance">
    <svg viewBox="0 0 56 56" fill="none" stroke="#fff" stroke-width="3"><path d="M8 48h40"/><rect x="12" y="32" width="7" height="14"/><rect x="24" y="24" width="7" height="22"/><rect x="36" y="16" width="7" height="30"/><path d="M10 24l12-10 8 6 14-12"/></svg>
    <h3>Finance</h3>
    <p>Budgeting, forecasting, cost control and funding support that give leaders a clear view of performance and the confidence to plan ahead.</p>
    <a class="more" href="#">Read more »</a>
  </div>
  <div class="service engineering">
    <svg viewBox="0 0 56 56" fill="none" stroke="#fff" stroke-width="3"><circle cx="22" cy="30" r="8"/><path d="M22 16v6M22 38v6M8 30h6M30 30h6M12 20l4 4M28 36l4 4M12 40l4-4M28 24l4-4"/><circle cx="42" cy="14" r="5"/><path d="M42 5v4M42 19v4M33 14h4M47 14h4"/></svg>
    <h3>Engineering</h3>
    <p>Project management, process improvement and technical reviews that help engineering teams deliver safely, on time and within budget every time.</p>
    <a class="more" href="#">Read more »</a>
  </div>
</section>

<section class="about">
  <div class="container">
    <div class="about-visual">
      <div class="about-screen" role="img" aria-label="Desktop monitor showing a photo of the consulting team at work"></div>
      <div class="about-stand"></div>
      <div class="about-base"></div>
    </div>
    <div class="about-copy">
      <h2>ABOUT KOBLANE</h2>
      <h4>Sed ut perspiciatis unde omnis iste natus error sit voluptatem accusantium doloremque</h4>
      <p>Koblane (Pty) Ltd was founded by a small group of consultants who believed that sound advice should be practical, honest and clearly explained. Since then we have helped clients across many sectors improve the way they work.</p>
      <p>Our team brings together specialists in information technology, finance and engineering. Each discipline is led by an experienced consultant who works closely with clients from the first meeting through to final delivery.</p>
      <p>We listen first, study the numbers and processes carefully, and then recommend changes that are realistic for your business. The result is lasting improvement rather than reports that sit on a shelf.</p>
      <a class="btn btn-solid" href="#">Read More</a>
    </div>
  </div>
</section>

<section class="testimonials">
  <h2 class="section-title">Testimonials</h2>
  <div class="rule"></div>
  <blockquote>
    <svg class="quote-mark" width="14" height="12" viewBox="0 0 14 12" fill="#0492cd"><path d="M0 12V6C0 2 2 0 5 0v2C3 2 2.5 3.5 2.5 5H5v7zM8 12V6c0-4 2-6 5-6v2c-2 0-2.5 1.5-2.5 3H13v7z"/></svg>Koblane gave our management team a clear picture of where money and time were being lost. Their consultants were patient, thorough and easy to work with, and the changes they recommended were simple to put in place. Within six months our reporting was faster, our costs were lower and our staff felt far more confident about the systems they use every day.
    <cite>JOHN DOE</cite>
    <span class="role">Managing Director</span>
  </blockquote>
  <div class="dots"><span class="on"></span><span></span><span></span></div>
</section>

<section class="news">
  <div class="container">
    <h2 class="section-title">Recent News</h2>
    <div class="rule"></div>
    <div class="news-list">
      <article class="news-item">
        <div class="news-date"><span class="day">SEP 01</span><span class="year">2015</span></div>
        <div><h5>Sed ut perspiciatis unde omnis</h5><p>A short update on new advisory services for small and medium businesses this season.</p></div>
      </article>
      <article class="news-item">
        <div class="news-date"><span class="day">SEP 01</span><span class="year">2015</span></div>
        <div><h5>Sed ut perspiciatis unde omnis</h5><p>Our finance team shares practical tips for tighter budgeting and better cash flow planning.</p></div>
      </article>
      <article class="news-item">
        <div class="news-date"><span class="day">SEP 01</span><span class="year">2015</span></div>
        <div><h5>Sed ut perspiciatis unde omnis</h5><p>Engineering review highlights on safer project delivery and improved site reporting.</p></div>
      </article>
    </div>
  </div>
</section>

<footer class="site-footer">
  <div class="container">
    <div class="foot-col col-links">
      <h6>Links</h6>
      <ul><li>Home</li><li>About Us</li><li>Services</li><li>Testimonials</li><li>News</li><li>Contact Us</li></ul>
    </div>
    <div class="foot-col col-news">
      <h6>Subscribe Our Newsletter</h6>
      <p>Sign Up Your Email In to Get Information<br>About Us</p>
      <div class="news-input">Email Address</div>
      <a class="btn btn-solid" href="#">Sign In</a>
    </div>
    <div class="foot-col col-follow">
      <h6>Follow Us On</h6>
      <ul class="social">
        <li><span class="icon-dot"></span>Friendbook</li>
        <li><span class="icon-dot"></span>Chirper</li>
        <li><span class="icon-dot"></span>Circles Plus</li>
        <li><span class="icon-dot"></span>ProLink</li>
      </ul>
    </div>
    <div class="foot-col col-contact">
      <h6>Contact Us</h6>
      <ul class="contact">
        <li><svg viewBox="0 0 14 14" fill="#33a6d7"><path d="M7 0a5 5 0 0 0-5 5c0 4 5 9 5 9s5-5 5-9a5 5 0 0 0-5-5zm0 7a2 2 0 1 1 0-4 2 2 0 0 1 0 4z"/></svg>Unit 12, Harbour View Park, 48 Ridge Road<br>Durban 4001, South Africa</li>
        <li><svg viewBox="0 0 14 14" fill="#33a6d7"><path d="M3 1l2.5 3-1.5 1.5c.8 1.8 2.2 3.2 4 4L9.5 8 13 10.5 11.5 13C6 13 1 8 1 2.5z"/></svg>+27 31 555 0142</li>
        <li><svg viewBox="0 0 14 14" fill="none" stroke="#33a6d7" stroke-width="1.5"><rect x="1" y="3" width="12" height="8"/><path d="M1 3l6 5 6-5"/></svg>info@koblane.example</li>
      </ul>
    </div>
  </div>
</footer>
<div class="copyright">Koblane (Pty) Ltd © 2015 . All rights reserved</div>

</body>
</html>
```